Fast Business Card Project

I need a business card with the name RENATO DUARTE stylized on one side and my email on the other (renatocosta4711@mailnova.com)

Industry/Entity Type

Business

Contact Information for Business Card

www.trilhamar.com.br

```html
<!DOCTYPE html>
<html lang="en">
<head>
<meta charset="utf-8">
<title>Renato Duarte – Business Card</title>
<link rel="stylesheet" href="https://fonts.googleapis.com/css2?family=Josefin+Sans:wght@300;400&display=swap">
<style>
  :root {
    --backdrop: #e9e6e1;
    --card-black: #1c1c1c;
    --card-black-soft: #2a2a2a;
    --gold-light: #f3e6a6;
    --gold-mid: #d9c27a;
    --gold-deep: #a8894a;
    --ring-dark: #232323;
    --shadow: rgba(0, 0, 0, 0.28);
  }
  * { box-sizing: border-box; margin: 0; padding: 0; }
  html, body {
    width: 1200px;
    height: 800px;
    overflow: hidden;
    background: var(--backdrop);
    font-family: "Josefin Sans", "Century Gothic", sans-serif;
  }
  .canvas {
    position: relative;
    width: 1200px;
    height: 800px;
  }
  .card {
    position: absolute;
    top: 258px;
    width: 500px;
    height: 285px;
    background: var(--card-black);
    box-shadow: 0 14px 30px var(--shadow);
    overflow: hidden;
  }
  .card--front { left: 70px; }
  .card--back { left: 630px; }

  .card__pattern {
    position: absolute;
    inset: 0;
    background: radial-gradient(circle at 50% 50%, var(--card-black-soft) 0%, var(--card-black) 70%);
  }
  .card__band {
    position: absolute;
    top: 0;
    width: 34px;
    height: 100%;
    background: linear-gradient(180deg, var(--gold-deep) 0%, var(--gold-light) 45%, var(--gold-mid) 70%, var(--gold-deep) 100%);
  }
  .card__band--left { left: 0; }
  .card__band--right { right: 0; }

  .emblem {
    position: absolute;
    left: 50%;
    top: 50%;
    width: 360px;
    height: 270px;
    transform: translate(-50%, -50%);
  }
  .emblem svg { position: absolute; inset: 0; }
  .emblem__name {
    position: absolute;
    left: 50%;
    top: 50%;
    transform: translate(-50%, -50%);
    white-space: nowrap;
    font-weight: 300;
    font-size: 23px;
    letter-spacing: 0.5px;
    line-height: 1;
    padding-top: 3px;
    color: var(--ring-dark);
  }

  .card__content {
    position: absolute;
    left: 62px;
    top: 92px;
    color: var(--gold-mid);
  }
  .card__name {
    font-weight: 300;
    font-size: 40px;
    letter-spacing: 0.5px;
    line-height: 1;
    white-space: nowrap;
    color: var(--gold-light);
  }
  .card__email {
    margin-top: 34px;
    font-weight: 400;
    font-size: 17px;
    letter-spacing: 0.4px;
    text-transform: uppercase;
    white-space: nowrap;
    color: var(--gold-mid);
  }
</style>
</head>
<body>
<main class="canvas">

  <section class="card card--front" aria-label="Business card front">
    <div class="card__pattern" role="img" aria-label="Faint dark ornamental pattern"></div>
    <div class="card__band card__band--left"></div>
    <div class="card__band card__band--right"></div>
    <div class="emblem">
      <svg viewBox="0 0 360 270" width="360" height="270" aria-hidden="true">
        <defs>
          <linearGradient id="emblemGold" x1="0" y1="0" x2="0" y2="1">
            <stop offset="0" stop-color="#f5eab0"/>
            <stop offset="0.55" stop-color="#dcc57e"/>
            <stop offset="1" stop-color="#b8985a"/>
          </linearGradient>
        </defs>
        <polygon points="30,135 62,119 62,151" fill="url(#emblemGold)"/>
        <polygon points="330,135 298,119 298,151" fill="url(#emblemGold)"/>
        <circle cx="180" cy="135" r="128" fill="none" stroke="#d9c27a" stroke-width="2"/>
        <circle cx="180" cy="135" r="122" fill="#232323"/>
        <circle cx="180" cy="135" r="114" fill="url(#emblemGold)"/>
      </svg>
      <div class="emblem__name">RENATO DUARTE</div>
    </div>
  </section>

  <section class="card card--back" aria-label="Business card back">
    <div class="card__pattern" role="img" aria-label="Faint dark ornamental pattern"></div>
    <div class="card__band card__band--left"></div>
    <div class="card__band card__band--right"></div>
    <div class="card__content">
      <h1 class="card__name">RENATO DUARTE</h1>
      <p class="card__email">renatocosta4711@mailnova.com</p>
    </div>
  </section>

</main>
</body>
</html>
```